Real Estate Wordpress Landing Page

I'm looking to a landing page dedicated to my real estate brokerage that's catered to promoting that my company provides 1.5% listings to home sellers... I have a couple examples that I'm really looking towards mocking in a version with similar color schemes using my current company colors/website.

http://lorvanta.com/
https://www.bluthorn.com/about/one-percent-listing-fee

My brokerage company website is http://www.calmridge.us/

Target Market(s)

real estate home sellers & buyers

Industry/Entity Type

Real Estate

Coding

Coded - Design and coding required

Number of Pages Required

1 page

Colors
3176b5
0255a3
eaf1f7
cedeed

Requirements
Must have
• Company website colors - http://www.calmridge.us/
• Something around the lines of this website page - http://lorvanta.com/
• Wordpress compatibility

```html
<!DOCTYPE html>
<html lang="en">
<head>
<meta charset="utf-8">
<title>Calmridge Realty – List for 1.5% Commission</title>
<link href="https://fonts.googleapis.com/css2?family=Montserrat:wght@400;500;600&family=Lato:ital,wght@0,400;0,700;1,700&family=Roboto+Condensed:wght@400;700&display=swap" rel="stylesheet">
<style>
:root{
  --blue:#0255a3;
  --blue-mid:#3176b5;
  --blue-bright:#2348ee;
  --pale:#eaf1f7;
  --line:#cedeed;
  --ink:#222;
  --grey:#666;
  --dark:#1b1b1b;
  --red:#d3171c;
  --green:#5cb85c;
  --white:#fff;
}
*{box-sizing:border-box;margin:0;padding:0}
html,body{width:1200px;height:2667px;overflow:hidden;background:var(--white)}
body{position:relative;font-family:'Lato',sans-serif;color:var(--ink)}
.abs{position:absolute}

/* top bar */
.topbar{left:0;top:0;width:1200px;height:32px;background:var(--dark);color:#ddd;font-size:11px}
.topbar .item{position:absolute;top:9px;display:flex;align-items:center;gap:8px}
.topbar svg{width:12px;height:12px;fill:#ccc}

/* hero */
.hero-bg{left:0;top:32px;width:1200px;height:555px;background:linear-gradient(180deg,#fafafa 0%,#e4e6e8 55%,#f0f1f2 100%)}
.brand{left:170px;top:52px;display:flex;align-items:center;gap:10px;font-family:'Montserrat',sans-serif;font-weight:600;font-size:24px;color:var(--blue)}
.brand .mark{width:26px;height:26px;background:var(--blue-bright)}
.hero-mark{left:555px;top:200px;width:90px;height:90px;border-radius:50%;background:var(--blue-bright)}
.headline{left:0;width:1200px;top:378px;text-align:center;font-family:'Montserrat',sans-serif;font-weight:500;font-size:44px;letter-spacing:1px;color:#1a1a1a}
.subline{left:0;width:1200px;top:432px;text-align:center;font-family:'Montserrat',sans-serif;font-size:18px;color:var(--blue)}

/* listing cards */
.listing{width:262px;height:190px;background:var(--white);padding:5px;box-shadow:0 1px 4px rgba(0,0,0,.15)}
.photo{position:relative;width:100%;height:100%;background:linear-gradient(180deg,#7fb2e0 0%,#b9c9d3 40%,#8c9a6e 75%,#5d7040 100%)}
.photo.kitchen{background:linear-gradient(180deg,#c9c4bb 0%,#8d8a86 45%,#5b5753 100%)}
.photo.villa{background:linear-gradient(180deg,#8fc0ec 0%,#e3d4b4 50%,#9aa373 100%)}
.caption{position:absolute;left:0;right:0;bottom:0;padding:5px 6px;background:rgba(20,20,20,.65);color:var(--white);font-family:'Roboto Condensed',sans-serif;font-size:11px;line-height:1.25;text-align:center;text-transform:uppercase}
.caption.blue{background:rgba(2,85,163,.88)}
.saved{position:absolute;left:13px;top:72px;width:50px;height:44px;background:var(--red);border:2px solid #fff;color:#fff;font-family:'Roboto Condensed',sans-serif;font-weight:700;font-size:10px;line-height:1.3;text-align:center;padding-top:8px}
.arrow{width:24px;height:40px;background:var(--blue-bright);display:flex;align-items:center;justify-content:center}
.arrow.left{border-radius:20px 0 0 20px}
.arrow.right{border-radius:0 20px 20px 0}
.arrow svg{width:10px;height:14px;fill:none;stroke:#fff;stroke-width:2.4}

/* broker */
.broker{left:172px;top:756px;width:824px;height:248px;border-radius:24px;background:linear-gradient(90deg,#fff 0%,var(--pale) 100%);box-shadow:0 2px 8px rgba(0,0,0,.12)}
.broker-mark{left:412px;top:738px;width:38px;height:38px;background:var(--blue-bright)}
.broker-house{left:980px;top:830px;width:190px;height:120px;background:linear-gradient(180deg,#f0f0f0,#fafafa)}
.broker-name{left:201px;top:780px;font-family:'Montserrat',sans-serif;font-weight:500;font-size:18px;color:#222}
.broker-role{left:201px;top:800px;font-family:'Montserrat',sans-serif;font-weight:500;font-size:31px;letter-spacing:1px;color:var(--blue)}
.broker-copy{left:201px;top:850px;font-size:14px;line-height:19px;color:#555}
.cta-bar{left:201px;top:901px;width:600px;height:34px;border-radius:17px 0 0 17px;background:var(--blue);color:#fff;font-style:italic;font-weight:700;font-size:20px;padding:5px 0 0 16px}
.broker-rule{left:201px;top:948px;width:580px;height:1px;background:var(--line)}
.contact-row{left:201px;top:955px;display:flex;align-items:center;font-size:20px;color:#333}
.contact-row .web{margin-left:40px;font-size:15px}
.ring{width:24px;height:24px;border:1.5px solid #999;border-radius:50%;display:inline-flex;align-items:center;justify-content:center;margin-right:12px}
.ring svg{width:12px;height:12px;fill:#888}
.socials{display:flex;gap:10px}
.socials span{width:18px;height:18px;border-radius:50%}
.portrait-ring{left:777px;top:750px;width:252px;height:252px;border-radius:50%;background:var(--blue);padding:8px}
.portrait{width:100%;height:100%;border-radius:50%;border:5px solid #fff;background:linear-gradient(180deg,#f2f2f2 0%,#cfcfcf 55%,#3c3c3c 100%);position:relative}
.portrait-name{position:absolute;left:0;right:0;bottom:42px;text-align:center;color:#fff;font-family:'Lato',sans-serif;font-weight:700;font-size:17px}

/* divider */
.divider{left:0;width:1200px;height:1px;background:#e2e2e2}
.notch{width:14px;height:8px}

/* guarantee */
.g-title{left:0;width:1200px;top:1108px;text-align:center;font-family:'Montserrat',sans-serif;font-size:27px;color:var(--blue)}
.g-title small{font-size:19px;color:#333}
.g-sub{left:0;width:1200px;top:1142px;text-align:center;font-family:'Montserrat',sans-serif;font-size:18px;color:#444}

/* services */
.service{width:262px;height:475px;background:#f1f5f9;box-shadow:0 1px 3px rgba(0,0,0,.1)}
.service .shot{position:absolute;left:8px;top:7px;width:246px;height:178px}
.service h3{position:absolute;left:0;right:0;top:214px;text-align:center;font-family:'Roboto Condensed',sans-serif;font-weight:700;font-size:17px;color:#1a1a1a;text-transform:uppercase}
.service ul{position:absolute;left:16px;right:14px;top:262px;list-style:none}
.service li{position:relative;padding-left:24px;font-size:11px;line-height:14px;margin-bottom:12px;color:#333}
.service li svg{position:absolute;left:0;top:1px;width:12px;height:11px;fill:none;stroke:#2f9a3a;stroke-width:2.5}
.service .note{position:absolute;left:16px;right:14px;top:378px;font-size:11px;line-height:14px;color:#888}
.btn{position:absolute;top:420px;height:30px;border-radius:4px;color:#fff;font-size:12px;display:flex;align-items:center;justify-content:center}
.btn.call{left:16px;width:109px;background:var(--blue)}
.btn.phone{left:144px;width:105px;background:var(--green)}

/* about */
.about-brand{left:0;width:1200px;top:1792px;display:flex;flex-direction:column;align-items:center;gap:8px;font-family:'Montserrat',sans-serif;font-weight:600;font-size:26px;color:#111}
.about-brand .mark{width:30px;height:30px;background:var(--blue-bright)}
.about-copy{left:178px;top:1902px;width:844px;text-align:center;font-size:11.5px;line-height:17px;color:#888}
.feature{width:240px;text-align:center;font-family:'Montserrat',sans-serif;font-size:15px;color:#222}
.feature .circle{width:70px;height:70px;margin:0 auto 22px;border-radius:50%;background:#eee;box-shadow:inset 0 0 0 2px #e0e0e0;display:flex;align-items:center;justify-content:center}
.feature svg{width:38px;height:38px;fill:none;stroke:var(--blue);stroke-width:2.2;stroke-linejoin:round}
.vrule{width:1px;height:110px;background:#ddd}

/* footer */
.skyline{left:280px;top:2185px;width:640px;height:66px;background:linear-gradient(180deg,rgba(40,40,40,.15),#1e1e1e)}
.footer{left:0;top:2251px;width:1200px;height:416px;background:var(--dark)}
.f-head{font-family:'Montserrat',sans-serif;font-size:18px;color:#fff}
.f-rule{height:1px;background:#333}
.f-item{display:flex;gap:18px;color:#ddd;font-size:13px;line-height:18px}
.f-icon{width:22px;height:22px;border-radius:50%;background:var(--blue-bright);display:flex;align-items:center;justify-content:center;flex:none}
.f-icon svg{width:11px;height:11px;fill:#fff}
.map{left:460px;top:2343px;width:255px;height:174px;border:4px solid #eee;background:linear-gradient(135deg,#e8e4da,#d9d4c5 60%,#e6c27a)}
.f-brand{left:228px;top:2575px;width:40px;height:40px;background:#bbb;opacity:.6}
.copyright{left:174px;top:2625px;font-size:10px;color:#999}
.f-socials{left:462px;top:2618px;display:flex;gap:13px}
.f-socials span{width:20px;height:20px;border-radius:50%}

/* form */
.form-panel{left:761px;top:2199px;width:267px;height:468px}
.form-title{left:761px;top:2258px;width:267px;text-align:center;font-family:'Montserrat',sans-serif;font-weight:500;font-size:17px;line-height:22px;color:#fff}
.field{left:775px;width:237px;height:31px;background:#fff;border-radius:2px;font-size:10px;color:#555;padding:10px 8px}
.field.notes{height:50px}
.submit{left:775px;top:2569px;width:237px;height:41px;background:var(--red);color:#fff;font-family:'Montserrat',sans-serif;font-size:16px;display:flex;align-items:center;justify-content:center}
</style>
</head>
<body>

<!-- top bar -->
<div class="abs topbar">
  <div class="item" style="left:468px"><svg viewBox="0 0 24 24"><path d="M6.6 10.8a15.1 15.1 0 0 0 6.6 6.6l2.2-2.2c.3-.3.7-.4 1-.2 1.1.4 2.3.6 3.6.6.6 0 1 .4 1 1V20c0 .6-.4 1-1 1C10.6 21 3 13.4 3 4c0-.6.4-1 1-1h3.5c.6 0 1 .4 1 1 0 1.3.2 2.5.6 3.6.1.3 0 .7-.2 1z"/></svg>555-310-4827</div>
  <div class="item" style="left:610px"><svg viewBox="0 0 24 24"><path d="M2 5h20v14H2zM2 5l10 8 10-8"/></svg>contact@calmridge.us</div>
  <div class="item" style="left:782px"><svg viewBox="0 0 24 24"><path d="M12 2a7 7 0 0 0-7 7c0 5 7 13 7 13s7-8 7-13a7 7 0 0 0-7-7zm0 9.5A2.5 2.5 0 1 1 12 6.5a2.5 2.5 0 0 1 0 5z"/></svg>2400 Harbor Point Dr, Ste 310, Coral Vista, FL 33426</div>
</div>

<!-- hero -->
<div class="abs hero-bg" role="img" aria-label="Pale white 3D city skyline backdrop"></div>
<div class="abs brand"><span class="mark"></span>Calmridge Realty</div>
<div class="abs hero-mark"></div>
<h1 class="abs headline">LIST FOR 1.5% COMMISSION,</h1>
<p class="abs subline">And Receive Top Marketing from Real Estate Pro!</p>

<div class="abs arrow left" style="left:151px;top:555px"><svg viewBox="0 0 10 14"><path d="M8 1 2 7l6 6"/></svg></div>
<div class="abs arrow right" style="left:1026px;top:555px"><svg viewBox="0 0 10 14"><path d="M2 1l6 6-6 6"/></svg></div>

<div class="abs listing" style="left:174px;top:494px">
  <div class="photo" role="img" aria-label="Two-storey house with palm tree">
    <div class="saved">SAVED<br>$4,650</div>
    <div class="caption">4218 Willow Brook Lane Fernhaven,<br>FL 33463 - $310,000</div>
  </div>
</div>
<div class="abs listing" style="left:468px;top:494px">
  <div class="photo kitchen" role="img" aria-label="Modern kitchen with stainless appliances">
    <div class="saved">SAVED<br>$7,485</div>
    <div class="caption">318 Palm Terrace Boulevard, 202 Coral<br>Vista, FL 33435 - $499,000</div>
  </div>
</div>
<div class="abs listing" style="left:761px;top:494px">
  <div class="photo villa" role="img" aria-label="Beige two-storey home with palms">
    <div class="saved">SAVED<br>$4,650</div>
    <div class="caption">10215 Stonegate Circle Fernhaven,<br>FL 33449 - $310,000</div>
  </div>
</div>

<!-- broker -->
<div class="abs broker-house" role="img" aria-label="Faint house outline decoration"></div>
<div class="abs broker"></div>
<div class="abs broker-mark"></div>
<div class="abs broker-name">MARCUS ELLERY, LIC.</div>
<div class="abs broker-role">REAL ESTATE BROKER</div>
<p class="abs broker-copy">On average, our customers save $5,600 when they list with us...<br>and they still receive top marketing and quality professional service!</p>
<div class="abs cta-bar">CALL US TODAY AND SAVE THOUSANDS $$</div>
<div class="abs broker-rule"></div>
<div class="abs contact-row">
  <span class="ring"><svg viewBox="0 0 24 24"><path d="M6.6 10.8a15.1 15.1 0 0 0 6.6 6.6l2.2-2.2c.3-.3.7-.4 1-.2 1.1.4 2.3.6 3.6.6.6 0 1 .4 1 1V20c0 .6-.4 1-1 1C10.6 21 3 13.4 3 4c0-.6.4-1 1-1h3.5c.6 0 1 .4 1 1 0 1.3.2 2.5.6 3.6.1.3 0 .7-.2 1z"/></svg></span>555-310-4827
  <span class="ring" style="margin-left:40px"><svg viewBox="0 0 24 24"><path d="M2 5h20v14H2z"/></svg></span><span style="font-size:15px">www.calmridge.us</span>
  <span class="socials" style="margin-left:54px">
    <span style="background:#3b5998"></span><span style="background:#dd4b39"></span><span style="background:#1da1f2"></span><span style="background:#0077b5"></span><span style="background:#cc181e"></span><span style="background:#c13584"></span>
  </span>
</div>
<div class="abs portrait-ring">
  <div class="portrait" role="img" aria-label="Portrait of the broker in a dark suit">
    <div class="portrait-name">Marcus Ellery</div>
  </div>
</div>

<div class="abs divider" style="top:1061px"></div>
<svg class="abs notch" style="left:593px;top:1061px" viewBox="0 0 14 8"><path d="M0 0h14L7 7z" fill="#fff" stroke="#e2e2e2"/></svg>

<!-- guarantee -->
<h2 class="abs g-title">30 Day Listing Service GUARANTEED. <small>Save thousands $$$ listing with us!</small></h2>
<p class="abs g-sub">Morbi eu sem felis. Integer faucibus ligula vitae enim vestibulum iaculis.</p>

<div class="abs service" style="left:174px;top:1209px">
  <div class="photo shot" role="img" aria-label="Two-storey house with palm tree">
    <div class="saved">SAVED<br>$4,200</div>
    <div class="caption blue">507 Orchard Club Drive Baymont,<br>FL 33462 $550,000</div>
  </div>
  <h3>Sell with Calmridge &amp; Save $$$</h3>
  <ul>
    <li><svg viewBox="0 0 12 11"><path d="M1 6l3.5 3.5L11 1"/></svg>Professional Real Estate Photography</li>
    <li><svg viewBox="0 0 12 11"><path d="M1 6l3.5 3.5L11 1"/></svg>Complimentary Comparative Market Analysis (CMA)</li>
    <li><svg viewBox="0 0 12 11"><path d="M1 6l3.5 3.5L11 1"/></svg>FREE Consultation with Real Estate Professional</li>
  </ul>
  <p class="note">Lorem ipsum dolor sit amet, consectetur adipiscing elit. Praesent rhoncus nibh nisl</p>
  <div class="btn call">CALL US!</div><div class="btn phone">555-310-4827</div>
</div>

<div class="abs service" style="left:468px;top:1209px">
  <div class="photo kitchen shot" role="img" aria-label="Modern kitchen with stainless appliances">
    <div class="saved">SAVED<br>$4,200</div>
    <div class="caption blue">318 Palm Terrace Boulevard, 202 Coral<br>Vista, FL 33435 - $499,000</div>
  </div>
  <h3>Start your home search with us</h3>
  <ul>
    <li><svg viewBox="0 0 12 11"><path d="M1 6l3.5 3.5L11 1"/></svg>1% Buyer Credit at Closing from Calmridge Realty</li>
    <li><svg viewBox="0 0 12 11"><path d="M1 6l3.5 3.5L11 1"/></svg>Quis Molestie Turpis Dapibus At</li>
    <li><svg viewBox="0 0 12 11"><path d="M1 6l3.5 3.5L11 1"/></svg>Quis Molestie Turpis Dapibus At</li>
  </ul>
  <p class="note">Lorem ipsum dolor sit amet, consectetur adipiscing elit. Praesent rhoncus nibh nisl</p>
  <div class="btn call">CALL US!</div><div class="btn phone">555-310-4827</div>
</div>

<div class="abs service" style="left:761px;top:1209px">
  <div class="photo villa shot" role="img" aria-label="Beige two-storey home with palms">
    <div class="saved">SAVED<br>$8,250</div>
    <div class="caption blue">507 Orchard Club Drive Baymont,<br>FL 33462 $550,000</div>
  </div>
  <h3>Leasing &amp; Property Managemen</h3>
  <ul>
    <li><svg viewBox="0 0 12 11"><path d="M1 6l3.5 3.5L11 1"/></svg>We can manage your rental portfolio for you!</li>
    <li><svg viewBox="0 0 12 11"><path d="M1 6l3.5 3.5L11 1"/></svg>Professional &amp; Experienced Property Managers</li>
    <li><svg viewBox="0 0 12 11"><path d="M1 6l3.5 3.5L11 1"/></svg>Receive Top Dollar for your Rental Properties</li>
  </ul>
  <p class="note">Lorem ipsum dolor sit amet, consectetur adipiscing elit. Praesent rhoncus nibh nisl</p>
  <div class="btn call">CALL US!</div><div class="btn phone">555-310-4827</div>
</div>

<div class="abs divider" style="top:1737px"></div>
<svg class="abs notch" style="left:593px;top:1737px" viewBox="0 0 14 8"><path d="M0 0h14L7 7z" fill="#fff" stroke="#e2e2e2"/></svg>

<!-- about -->
<div class="abs about-brand"><span class="mark"></span>Calmridge Realty</div>
<p class="abs about-copy">Calmridge Realty is a Coral Vista real estate company that prides in our superior service when it comes to helping our clients buy a home, sell a home or rent a home in the Seagrove County and Alder County areas. We have vast knowledge in these areas and can provide you, as a client, a comforting and smooth real estate transaction.</p>

<div class="abs feature" style="left:223px;top:1995px">
  <div class="circle"><svg viewBox="0 0 40 40"><path d="M8 6v30M8 8h24M14 8v4M26 8v4M12 12h16v14H12z"/><path d="M15 24v-6l5-4 5 4v6z"/></svg></div>BUY A HOME
</div>
<div class="abs vrule" style="left:475px;top:1990px"></div>
<div class="abs feature" style="left:479px;top:1995px">
  <div class="circle"><svg viewBox="0 0 40 40"><path d="M6 18 20 6l14 12M10 15v8M30 15v8"/><path d="M12 22h16v10H12z"/></svg></div>SELL A HOME
</div>
<div class="abs vrule" style="left:735px;top:1990px"></div>
<div class="abs feature" style="left:764px;top:1995px">
  <div class="circle"><svg viewBox="0 0 40 40"><path d="M8 20 20 9l12 11M12 17v15h16V17"/><circle cx="20" cy="22" r="3"/><path d="M20 25v5"/></svg></div>RENT A HOME
</div>

<!-- footer -->
<div class="abs skyline" role="img" aria-label="Dark city skyline silhouette"></div>
<div class="abs footer"></div>

<div class="abs f-head" style="left:174px;top:2291px">GET IN TOUCH</div>
<div class="abs f-rule" style="left:174px;top:2322px;width:250px"></div>
<div class="abs f-item" style="left:174px;top:2340px"><span class="f-icon"><svg viewBox="0 0 24 24"><path d="M12 2a7 7 0 0 0-7 7c0 5 7 13 7 13s7-8 7-13a7 7 0 0 0-7-7z"/></svg></span>2400 Harbor Point Dr, Suite 310<br>Coral Vista,<br>FL 33426</div>
<div class="abs f-item" style="left:174px;top:2419px;font-size:22px;line-height:24px;color:#fff"><span class="f-icon"><svg viewBox="0 0 24 24"><path d="M6.6 10.8a15.1 15.1 0 0 0 6.6 6.6l2.2-2.2c.3-.3.7-.4 1-.2 1.1.4 2.3.6 3.6.6.6 0 1 .4 1 1V20c0 .6-.4 1-1 1C10.6 21 3 13.4 3 4c0-.6.4-1 1-1h3.5c.6 0 1 .4 1 1 0 1.3.2 2.5.6 3.6.1.3 0 .7-.2 1z"/></svg></span>555-310-4827</div>
<div class="abs f-item" style="left:174px;top:2462px;font-size:12px"><span class="f-icon"><svg viewBox="0 0 24 24"><path d="M2 5h20v14H2z"/></svg></span>contact@calmridge.us</div>
<div class="abs f-item" style="left:174px;top:2503px;font-size:12px"><span class="f-icon"><svg viewBox="0 0 24 24"><circle cx="12" cy="12" r="9"/></svg></span>www.calmridge.us</div>
<div class="abs f-rule" style="left:174px;top:2558px;width:530px"></div>
<div class="abs f-brand"></div>
<div class="abs copyright">Calmridge.us - All rights reserved.</div>

<div class="abs f-head" style="left:460px;top:2291px">LOCATION MAP</div>
<div class="abs f-rule" style="left:460px;top:2322px;width:255px"></div>
<div class="abs map" role="img" aria-label="Street map with office location marker"></div>
<div class="abs f-head" style="left:462px;top:2582px">FOLLOW US</div>
<div class="abs f-socials">
  <span style="background:#2b5cb8"></span><span style="background:#1da1f2"></span><span style="background:#0077b5"></span><span style="background:#dd4b39"></span><span style="background:#cc181e"></span><span style="background:#bd081c"></span><span style="background:#c13584"></span><span style="background:#e05a26"></span>
</div>

<svg class="abs form-panel" viewBox="0 0 267 468"><path d="M0 50 133.5 0 267 50V468H0z" fill="#0255a3"/></svg>
<div class="abs form-title">TALK TO A LOCAL<br>BLUTHORN AGENT</div>
<div class="abs field" style="top:2343px">First Name*</div>
<div class="abs field" style="top:2384px">Email*</div>
<div class="abs field" style="top:2425px">Phone*</div>
<div class="abs field" style="top:2466px">Street Address*</div>
<div class="abs field notes" style="top:2507px">Notes</div>
<div class="abs submit">SUBMIT</div>

</body>
</html>
```